RK Bastone Construction Inc.

Design a new business card for our construction company
To be removed from current card:
Delete 25 years
Delete Tenant fit up Renovations section

```html
<!DOCTYPE html>
<html lang="en">
<head>
<meta charset="utf-8">
<title>RK Bastone Construction Inc. — Business Card</title>
<link rel="stylesheet" href="https://fonts.googleapis.com/css2?family=Montserrat:wght@500;600;700&family=Red+Hat+Display:wght@500;600&display=swap">
<style>
  :root {
    --purple: #532d6d;
    --purple-deep: #240f3a;
    --purple-ink: #4f2b6b;
    --teal: #23756a;
    --white: #ffffff;
    --page: #ffffff;
    --rule: #d9d9d9;
  }
  * { box-sizing: border-box; margin: 0; padding: 0; }
  html, body {
    width: 1020px;
    height: 1200px;
    overflow: hidden;
    background: var(--page);
  }
  .card {
    position: absolute;
    left: 160px;
    width: 696px;
    height: 426px;
    overflow: hidden;
  }
  /* Front side */
  .card--front {
    top: 127px;
    background: linear-gradient(90deg, var(--purple) 0%, #3a1c50 55%, var(--purple-deep) 100%);
  }
  .brand {
    position: absolute;
    left: 0;
    right: 0;
    text-align: center;
    color: var(--white);
    font-family: "Red Hat Display", sans-serif;
    font-weight: 600;
  }
  .brand__name {
    top: 210px;
    font-size: 44px;
    letter-spacing: 1px;
    line-height: 1;
  }
  .brand__suffix {
    top: 266px;
    font-size: 21px;
    letter-spacing: 4px;
    line-height: 1;
  }
  /* Back side */
  .card--back {
    top: 629px;
    background: var(--white);
    border: 1px solid var(--rule);
    border-bottom: none;
  }
  .card__band {
    position: absolute;
    inset: 0;
    width: 696px;
    height: 426px;
  }
  .holder__name {
    position: absolute;
    left: 50px;
    top: 36px;
    font-family: "Red Hat Display", sans-serif;
    font-weight: 500;
    font-size: 54px;
    letter-spacing: -2.5px;
    color: var(--purple-ink);
    line-height: 1;
  }
  .holder__phone {
    position: absolute;
    left: 55px;
    top: 93px;
    font-family: "Red Hat Display", sans-serif;
    font-weight: 500;
    font-size: 23px;
    letter-spacing: -0.5px;
    color: var(--purple-ink);
  }
  .services {
    position: absolute;
    left: 53px;
    top: 155px;
    list-style: none;
    font-family: "Montserrat", sans-serif;
    font-weight: 700;
    font-size: 24px;
    color: var(--purple-ink);
    line-height: 26px;
  }
  .services li {
    display: flex;
    align-items: center;
    gap: 7px;
  }
  .services li::before {
    content: "";
    width: 3px;
    height: 11px;
    background: var(--purple-ink);
  }
  .mini-brand {
    position: absolute;
    right: 60px;
    top: 80px;
    text-align: center;
    font-family: "Red Hat Display", sans-serif;
    font-weight: 600;
    color: var(--purple-ink);
    line-height: 1;
  }
  .mini-brand__name { font-size: 20px; letter-spacing: 0.5px; }
  .mini-brand__suffix { font-size: 9px; letter-spacing: 2px; margin-top: 4px; }
  .contact {
    position: absolute;
    font-family: "Red Hat Display", sans-serif;
    font-weight: 500;
    color: var(--white);
    letter-spacing: -0.4px;
  }
  .contact--office { left: 48px; top: 336px; }
  .contact__main { font-size: 25px; letter-spacing: -1px; line-height: 30px; }
  .contact__line { font-size: 16px; line-height: 22px; }
  .contact--address { left: 495px; top: 366px; }
</style>
</head>
<body>
  <section class="card card--front" aria-label="Card front">
    <div class="brand brand__name">RK BASTONE</div>
    <div class="brand brand__suffix">CONSTRUCTION INC.</div>
  </section>

  <section class="card card--back" aria-label="Card back">
    <svg class="card__band" viewBox="0 0 696 426" aria-hidden="true">
      <defs>
        <linearGradient id="bandFill" x1="0" y1="0" x2="1" y2="0">
          <stop offset="0" stop-color="#532d6d"/>
          <stop offset="0.55" stop-color="#3b5068"/>
          <stop offset="1" stop-color="#23756a"/>
        </linearGradient>
      </defs>
      <polygon points="0,293 605,347 675,0 696,0 696,426 0,426" fill="url(#bandFill)"/>
    </svg>

    <h1 class="holder__name">Marco Bastone</h1>
    <p class="holder__phone">613-555-0142</p>

    <ul class="services">
      <li>Turn Key Operations</li>
      <li>Project Management</li>
    </ul>

    <div class="mini-brand">
      <div class="mini-brand__name">RK BASTONE</div>
      <div class="mini-brand__suffix">CONSTRUCTION INC.</div>
    </div>

    <div class="contact contact--office">
      <div class="contact__main">613-555-0187</div>
      <div class="contact__line">www.rkbastoneconstruction.ca</div>
      <div class="contact__line">marco@rkbastoneconst.ca</div>
    </div>

    <address class="contact contact--address" style="font-style: normal;">
      <div class="contact__line">100-2210 Harlow Rd</div>
      <div class="contact__line">Ottawa, Ontario K1B 4T7</div>
    </address>
  </section>
</body>
</html>
```